Collage: Kunden in Coaching und Organisationsberatung

Ich brauche eine jederzeit mit herkömmlichen Programmen bearbeitbare Vorlage, um in sozialen Medien meine Kunden vorstellen zu können - damit zu erklären, wie Coaching und Organisationsberatung wirken kann. Diese Persona sollen in einer Collage mit passenden Bildern und Texten präsentiert werden können. Als grafische Orientierung kann meine Homepage https://www.lavirna.at/ dienen. Meine Farbcodes sind auf der Webseite - sprich digital RGB: Blau: #739fc7, Grün: #b8c830 und Orange: #cc610a; Im Print also CMYK: Blau: 70/20/10/0, Grün: 0/10/100/0 und Orange: 0/68/100/0; Texte sollen in folgender Länge Platz finden - diese Info dient nur zur Größenabschätzung der Platzhalter. Der Rest kann frei mit Bildern, Symbolen, ... gestaltet werden.
Textbeispiel 1:
Helga – Führungskraft mit Ambitionen und Herausforderungen
Alter: 42 Jahre
Funktion: Bereichsleiterin Finanzen in einem großen Dienstleistungsunternehmen
Lebenssituation: Verheiratet, zwei Kinder (Gymnasium, Unterstufe), Partner arbeitet als technischer Zeichner
🎯 Ziele & 🧭 Motive
• Will sich als moderne Führungskraft etablieren – mit Haltung, Vertrauen und Eigenverantwortung
• Strebt eine konstruktive, offene Kommunikation in ihrem Bereich an
• Möchte ihren Managementstil von operativer Detailarbeit hin zur strategischen Führung weiterentwickeln
• Sucht nach Balance zwischen Beruf, Familie und persönlichen Bedürfnissen
⚠️ Herausforderungen & Belastungen
• Übergang von Kollegin zu Vorgesetzter: Beziehungskonflikte und Rollenklarheit
• Kommunikationskultur im Team ist verschlossen und wenig kooperativ
• Hoher Anspruch an sich selbst – und an andere
• Rückfall in operative Aufgaben → Zeitdruck & Energieverlust
• Entscheidungsschwierigkeiten durch komplexe Abstimmungen und fehlende Klarheit über Stakeholder
• Innere Spannung zwischen Führungsanspruch und fehlendem methodischem Rüstzeug
💬 Typische Aussagen
• „Ich will nicht führen wie mein Vorgänger – das geht heute anders.“
• „Ich will, dass die Leute Verantwortung übernehmen und nicht nur ausführen.“
• „Manchmal bin ich zu ungeduldig – aber ich habe einfach keine Zeit für Umwege.“
• „Ich muss weg von der Detailarbeit – aber wie schaffe ich das wirklich?“
📌 Entwicklungsbedarfe
• Coaching zur Selbstklärung und Rollenentwicklung
• Training zu Kommunikation in Führung, Feedback- und Konfliktkultur
• Impulse zur Reflexion über Führungshaltung und Teamsteuerung
• Unterstützung im Aufbau eines kollaborativen Netzwerks innerhalb der Organisation
📣 Zielgruppenansprache (ProNetz-Kontext)
Diese Persona spricht Führungskräfte an, die:
• neu in ihrer Rolle sind (meist durch schnellen Aufstieg)
• den Willen zur Veränderung mitbringen, aber noch nicht das passende Werkzeug
• zwischen strategischem Anspruch und operativem Alltag aufgerieben werden
• Kommunikation, Führung und Selbstführung gleichzeitig lernen und leben wollen
Textbeispiel 2:
Herbert
Persona: Herbert – Fachlich stark, persönlich überfordert
Alter: 36 Jahre
Funktion: Bilanzbuchhalter in einer mittelgroßen Spedition
Position: Formal als Abteilungsleiter geführt – ohne kommunizierte Führungsverantwortung
Lebenssituation: Lebt allein, gelegentliche Beziehungserfahrungen
🎯 Ziele & 🧭 Motive
• Wünscht sich Stabilität, Struktur und fachlich saubere Arbeitsprozesse
• Möchte gute, fehlerfreie Arbeit leisten und professionell wahrgenommen werden
• Hat sich für diesen Job entschieden, um mehr Lebensqualität zu gewinnen
• Sehnt sich nach Klarheit in Rollen, Zuständigkeiten und Abläufen
• Ungeklärte Führungsrolle: Der Titel „Abteilungsleiter*“ verunsichert – es fehlt eine explizite Einordnung
• Überlastung durch chaotische Prozesse und laufende Systemumstellung
• Fehlende Unterstützung im Team – insbesondere durch eine überforderte Kollegin
• Schwierigkeiten, Grenzen zu setzen oder Klarheit einzufordern – v. a. gegenüber Führungskraft und Kolleg*innen
• Perfektionismus führt zu Überstunden, Schlafproblemen und emotionaler Erschöpfung
• Geringe Sichtbarkeit im Betrieb – kaum Kommunikation außerhalb des Büros
• Hohes Bedürfnis nach Kontrolle steht einem agilen Umfeld entgegen
💬 Typische Aussagen
• „Ich bin kein Abteilungsleiter – ich habe das nie gewollt.“
• „Ich will einfach gute Arbeit machen – aber so geht das nicht.“
• „Ich habe keine Zeit, das Chaos zu ordnen – ich bin zu sehr damit beschäftigt, es auszuhalten.“
• „Coaching? Vielleicht bringt es ja wenigstens etwas Struktur in meine Gedanken.“
📌 Entwicklungsbedarfe
• Klärung der eigenen beruflichen Rolle und Abgrenzung zur Führungsverantwortung
• Unterstützung beim Umgang mit Unklarheit und Perfektionismus
• Stärkung der Selbstführung und Kommunikation im System
• Strukturierungshilfen im Arbeitsalltag – Priorisierung, Delegation, Nein-Sagen
• Entlastung durch Reflexion – Reduktion von Selbstüberforderung
• Ermutigung zur Klärung mit Führungskraft (z. B. über ein geleitetes Gespräch oder systemisches Rollenmodell)
Diese Persona spricht Mitarbeiter*innen an, die:
• fachlich sehr kompetent, aber systemisch überfordert sind
• sich in unklaren Rollen- und Erwartungsstrukturen wiederfinden
• zwischen Anspruch und Wirklichkeit leiden
• sich nach Struktur, Sicherheit und professioneller Entlastung sehnen
• Coaching als „letzte Möglichkeit“ sehen, ihre Gedanken zu ordnen und Klarheit zu gewinnen
LG und danke für die Vorschläge

```html
<!DOCTYPE html>
<html lang="de">
<head>
<meta charset="utf-8">
<title>lavirna – Persona Herbert</title>
<link href="https://fonts.googleapis.com/css2?family=Poppins:wght@200;300;400;600;700;800&display=swap" rel="stylesheet">
<style>
  :root{
    --blue:#739fc7;
    --blue-logo:#5a9ccc;
    --green:#b8c830;
    --panel:#e4e4e4;
    --ink:#111;
    --rule:#c9c9c9;
    --paper:#fff;
  }
  *{margin:0;padding:0;box-sizing:border-box}
  html,body{width:903px;height:1200px;overflow:hidden;background:var(--paper)}
  body{font-family:"Poppins",sans-serif;color:var(--ink);position:relative}

  .sidebar{position:absolute;left:58px;top:0;width:320px;height:1196px}
  .sidebar-panel{position:absolute;left:2px;top:300px;width:318px;height:896px;background:var(--panel)}
  .sidebar-band{position:absolute;left:0;top:0}
  .portrait{position:absolute;left:16px;top:127px;width:290px;height:290px;border-radius:50%;
    background:radial-gradient(circle at 50% 42%,#e9dccf 0%,#d8c3b0 30%,#f2f2f0 55%,#fafafa 100%)}

  .section-head{position:absolute;display:flex;align-items:center;gap:14px}
  .section-icon{width:40px;height:40px;border-radius:50%;background:var(--green);flex:none;display:flex;align-items:center;justify-content:center}
  .section-title{font-weight:700;font-size:20px;line-height:1.05}
  .section-title .sub{font-weight:300;display:block}

  .list{position:absolute;list-style:none}
  .list li{display:flex;gap:8px;line-height:1.17}
  .list li svg{flex:none;margin-top:2px}

  .list-left{left:21px;width:280px;font-size:11.6px}
  .list-left li{margin-bottom:12.5px}

  .rule{position:absolute;height:1px;background:var(--rule)}

  .brand{position:absolute;left:433px;top:56px;display:flex;align-items:center;gap:10px}
  .brand-name{font-weight:200;font-size:50px;letter-spacing:-1px;color:var(--ink);line-height:1}
  .brand-dot{width:26px;height:26px;border-radius:50%;background:var(--blue-logo)}

  .persona-name{position:absolute;left:432px;top:124px;font-weight:800;font-size:42px;color:var(--blue);line-height:1.1}
  .facts{position:absolute;left:433px;top:182px;width:420px;font-size:13.4px;line-height:1.2}
  .facts p{margin-bottom:13px}
  .facts b{font-weight:600}

  .list-right{left:433px;width:380px;font-size:10.4px}
  .list-right li{margin-bottom:10.5px}
</style>
</head>
<body>

<aside class="sidebar">
  <div class="sidebar-panel"></div>
  <svg class="sidebar-band" width="320" height="440" viewBox="0 0 320 440" aria-hidden="true">
    <circle cx="161" cy="272" r="172" fill="#fff"/>
    <path d="M0 0H320V272A160 160 0 0 1 0 272Z" fill="var(--blue)"/>
    <circle cx="161" cy="272" r="147" fill="#fff"/>
  </svg>
  <div class="portrait" role="img" aria-label="Porträtfoto der Persona Herbert, lächelnder Mann mit Brille im weißen Hemd"></div>

  <div class="section-head" style="left:21px;top:488px">
    <span class="section-icon"><svg width="22" height="22" viewBox="0 0 22 22" fill="none" stroke="#fff" stroke-width="1.4"><circle cx="11" cy="8" r="4"/><path d="M4 20c1-5 4-7 7-7s6 2 7 7"/></svg></span>
    <span class="section-title">Entwicklungsbedarfe</span>
  </div>
  <ul class="list list-left" style="top:546px">
    <li><svg width="11" height="11" viewBox="0 0 12 12"><circle cx="6" cy="6" r="6"/><path d="M3.2 6.2 5.2 8 8.8 4" stroke="#fff" stroke-width="1.5" fill="none"/></svg><span>Klärung der eigenen beruflichen Rolle und Abgrenzung zur Führungsverantwortung</span></li>
    <li><svg width="11" height="11" viewBox="0 0 12 12"><circle cx="6" cy="6" r="6"/><path d="M3.2 6.2 5.2 8 8.8 4" stroke="#fff" stroke-width="1.5" fill="none"/></svg><span>Unterstützung beim Umgang mit Unklarheit und Perfektionismus</span></li>
    <li><svg width="11" height="11" viewBox="0 0 12 12"><circle cx="6" cy="6" r="6"/><path d="M3.2 6.2 5.2 8 8.8 4" stroke="#fff" stroke-width="1.5" fill="none"/></svg><span>Stärkung der Selbstführung und<br>Kommunikation im System</span></li>
    <li><svg width="11" height="11" viewBox="0 0 12 12"><circle cx="6" cy="6" r="6"/><path d="M3.2 6.2 5.2 8 8.8 4" stroke="#fff" stroke-width="1.5" fill="none"/></svg><span>Strukturierungshilfen im Arbeitsalltag Priorisierung, Delegation, Nein-Sagen</span></li>
    <li><svg width="11" height="11" viewBox="0 0 12 12"><circle cx="6" cy="6" r="6"/><path d="M3.2 6.2 5.2 8 8.8 4" stroke="#fff" stroke-width="1.5" fill="none"/></svg><span>Entlastung durch Reflexion – Reduktion von Selbstüberforderung</span></li>
    <li><svg width="11" height="11" viewBox="0 0 12 12"><circle cx="6" cy="6" r="6"/><path d="M3.2 6.2 5.2 8 8.8 4" stroke="#fff" stroke-width="1.5" fill="none"/></svg><span>Ermutigung zur Klärung mit Führungskraft (z. B. über ein geleitetes Gespräch oder systemisches Rollenmodell)</span></li>
  </ul>
  <div class="rule" style="left:14px;top:818px;width:278px"></div>

  <div class="section-head" style="left:14px;top:862px;align-items:flex-start">
    <span class="section-icon"><svg width="22" height="22" viewBox="0 0 22 22" fill="none" stroke="#fff" stroke-width="1.4"><circle cx="11" cy="7" r="3"/><circle cx="5" cy="11" r="2"/><circle cx="17" cy="11" r="2"/><path d="M5 19c1-4 3-6 6-6s5 2 6 6"/></svg></span>
    <span class="section-title">Zielgruppenansprache<span class="sub">(ProNetz-Kontext)</span></span>
  </div>
  <ul class="list list-left" style="top:925px">
    <li><svg width="11" height="11" viewBox="0 0 12 12"><circle cx="6" cy="6" r="6"/><path d="M3.2 6.2 5.2 8 8.8 4" stroke="#fff" stroke-width="1.5" fill="none"/></svg><span>fachlich sehr kompetent, aber systemisch überfordert sind</span></li>
    <li><svg width="11" height="11" viewBox="0 0 12 12"><circle cx="6" cy="6" r="6"/><path d="M3.2 6.2 5.2 8 8.8 4" stroke="#fff" stroke-width="1.5" fill="none"/></svg><span>sich in unklaren Rollen- und Erwartungsstrukturen wiederfinden</span></li>
    <li><svg width="11" height="11" viewBox="0 0 12 12"><circle cx="6" cy="6" r="6"/><path d="M3.2 6.2 5.2 8 8.8 4" stroke="#fff" stroke-width="1.5" fill="none"/></svg><span>zwischen Anspruch und Wirklichkeit leiden</span></li>
    <li><svg width="11" height="11" viewBox="0 0 12 12"><circle cx="6" cy="6" r="6"/><path d="M3.2 6.2 5.2 8 8.8 4" stroke="#fff" stroke-width="1.5" fill="none"/></svg><span>sich nach Struktur, Sicherheit und professioneller Entlastung sehnen</span></li>
    <li><svg width="11" height="11" viewBox="0 0 12 12"><circle cx="6" cy="6" r="6"/><path d="M3.2 6.2 5.2 8 8.8 4" stroke="#fff" stroke-width="1.5" fill="none"/></svg><span>Coaching als „letzte Möglichkeit“ sehen, ihre Gedanken zu ordnen und Klarheit zu gewinnen</span></li>
    <li><svg width="11" height="11" viewBox="0 0 12 12"><circle cx="6" cy="6" r="6"/><path d="M3.2 6.2 5.2 8 8.8 4" stroke="#fff" stroke-width="1.5" fill="none"/></svg><span>LG und danke für die Vorschläg</span></li>
  </ul>
</aside>

<main>
  <div class="brand"><span class="brand-name">lavirna</span><span class="brand-dot"></span></div>
  <h1 class="persona-name">Herbert</h1>
  <div class="facts">
    <p><b>Persona:</b> Herbert – Fachlich stark, persönlich überfordert</p>
    <p><b>Alter:</b> 36 Jahre</p>
    <p><b>Funktion:</b> Bilanzbuchhalter in einer mittelgroßen Spedition</p>
    <p><b>Position:</b> Formal als Abteilungsleiter geführt – ohne<br>kommunizierte Führungsverantwortung</p>
    <p><b>Lebenssituation:</b> Lebt allein, gelegentliche<br>Beziehungserfahrungen</p>
  </div>
  <div class="rule" style="left:433px;top:371px;width:412px"></div>

  <div class="section-head" style="left:435px;top:389px">
    <span class="section-icon"><svg width="24" height="24" viewBox="0 0 24 24" fill="none" stroke="#fff" stroke-width="1.4"><circle cx="12" cy="12" r="9"/><circle cx="12" cy="12" r="5.5"/><circle cx="12" cy="12" r="2"/><path d="M12 12 20 4"/></svg></span>
    <span class="section-title">Ziele &amp; Motive</span>
  </div>
  <ul class="list list-right" style="top:446px">
    <li><svg width="10" height="10" viewBox="0 0 12 12"><circle cx="6" cy="6" r="6"/><path d="M3.2 6.2 5.2 8 8.8 4" stroke="#fff" stroke-width="1.5" fill="none"/></svg><span>Wünscht sich Stabilität, Struktur und fachlich saubere<br>Arbeitsprozesse</span></li>
    <li><svg width="10" height="10" viewBox="0 0 12 12"><circle cx="6" cy="6" r="6"/><path d="M3.2 6.2 5.2 8 8.8 4" stroke="#fff" stroke-width="1.5" fill="none"/></svg><span>Möchte gute, fehlerfreie Arbeit leisten und professionell<br>wahrgenommen werden</span></li>
    <li><svg width="10" height="10" viewBox="0 0 12 12"><circle cx="6" cy="6" r="6"/><path d="M3.2 6.2 5.2 8 8.8 4" stroke="#fff" stroke-width="1.5" fill="none"/></svg><span>Hat sich für diesen Job entschieden, um mehr Lebensqualität<br>zu gewinnen</span></li>
    <li><svg width="10" height="10" viewBox="0 0 12 12"><circle cx="6" cy="6" r="6"/><path d="M3.2 6.2 5.2 8 8.8 4" stroke="#fff" stroke-width="1.5" fill="none"/></svg><span>Sehnt sich nach Klarheit in Rollen, Zuständigkeiten und Abläufen</span></li>
  </ul>
  <div class="rule" style="left:433px;top:590px;width:412px"></div>

  <div class="section-head" style="left:435px;top:623px">
    <span class="section-icon"><svg width="22" height="22" viewBox="0 0 22 22" fill="none" stroke="#fff" stroke-width="1.4"><rect x="4" y="3" width="11" height="15" rx="1"/><path d="M7 7h5M7 10h5M7 13h3"/><circle cx="16" cy="16" r="3.5"/><path d="m14.5 16 1 1 2-2"/></svg></span>
    <span class="section-title">Herausforderungen &amp; Belastungen</span>
  </div>
  <ul class="list list-right" style="top:678px">
    <li><svg width="10" height="10" viewBox="0 0 12 12"><circle cx="6" cy="6" r="6"/><path d="M3.2 6.2 5.2 8 8.8 4" stroke="#fff" stroke-width="1.5" fill="none"/></svg><span>Ungeklärte Führungsrolle: Der Titel „Abteilungsleiter*“<br>verunsichert – es fehlt eine explizite Einordnung</span></li>
    <li><svg width="10" height="10" viewBox="0 0 12 12"><circle cx="6" cy="6" r="6"/><path d="M3.2 6.2 5.2 8 8.8 4" stroke="#fff" stroke-width="1.5" fill="none"/></svg><span>Überlastung durch chaotische Prozesse und laufende<br>Systemumstellung</span></li>
    <li><svg width="10" height="10" viewBox="0 0 12 12"><circle cx="6" cy="6" r="6"/><path d="M3.2 6.2 5.2 8 8.8 4" stroke="#fff" stroke-width="1.5" fill="none"/></svg><span>Fehlende Unterstützung im Team – insbesondere durch eine<br>überforderte Kollegin</span></li>
    <li><svg width="10" height="10" viewBox="0 0 12 12"><circle cx="6" cy="6" r="6"/><path d="M3.2 6.2 5.2 8 8.8 4" stroke="#fff" stroke-width="1.5" fill="none"/></svg><span>Schwierigkeiten, Grenzen zu setzen oder Klarheit einzufordern – v. a.<br>gegenüber Führungskraft und Kolleg*innen</span></li>
    <li><svg width="10" height="10" viewBox="0 0 12 12"><circle cx="6" cy="6" r="6"/><path d="M3.2 6.2 5.2 8 8.8 4" stroke="#fff" stroke-width="1.5" fill="none"/></svg><span>Perfektionismus führt zu Überstunden, Schlafproblemen und<br>emotionaler Erschöpfung</span></li>
    <li><svg width="10" height="10" viewBox="0 0 12 12"><circle cx="6" cy="6" r="6"/><path d="M3.2 6.2 5.2 8 8.8 4" stroke="#fff" stroke-width="1.5" fill="none"/></svg><span>Geringe Sichtbarkeit im Betrieb – kaum Kommunikation außerhalb<br>des Büros</span></li>
    <li><svg width="10" height="10" viewBox="0 0 12 12"><circle cx="6" cy="6" r="6"/><path d="M3.2 6.2 5.2 8 8.8 4" stroke="#fff" stroke-width="1.5" fill="none"/></svg><span>Hohes Bedürfnis nach Kontrolle steht einem agilen Umfeld entgegen</span></li>
  </ul>
  <div class="rule" style="left:433px;top:931px;width:412px"></div>

  <div class="section-head" style="left:435px;top:964px">
    <span class="section-icon"><svg width="22" height="22" viewBox="0 0 22 22" fill="none" stroke="#fff" stroke-width="1.4"><path d="M3 5h11v8H8l-3 3v-3H3z"/><path d="M16 9h3v7h-2v3l-3-3h-4"/></svg></span>
    <span class="section-title">Typische Aussagen</span>
  </div>
  <ul class="list list-right" style="top:1021px">
    <li><svg width="10" height="10" viewBox="0 0 12 12"><circle cx="6" cy="6" r="6"/><path d="M3.2 6.2 5.2 8 8.8 4" stroke="#fff" stroke-width="1.5" fill="none"/></svg><span>Ich bin kein Abteilungsleiter – ich habe das nie gewollt.“</span></li>
    <li><svg width="10" height="10" viewBox="0 0 12 12"><circle cx="6" cy="6" r="6"/><path d="M3.2 6.2 5.2 8 8.8 4" stroke="#fff" stroke-width="1.5" fill="none"/></svg><span>„Ich will einfach gute Arbeit machen – aber so geht das nicht.“</span></li>
    <li><svg width="10" height="10" viewBox="0 0 12 12"><circle cx="6" cy="6" r="6"/><path d="M3.2 6.2 5.2 8 8.8 4" stroke="#fff" stroke-width="1.5" fill="none"/></svg><span>„Ich habe keine Zeit, das Chaos zu ordnen – ich bin zu sehr damit<br>beschäftigt, es auszuhalten.“</span></li>
    <li><svg width="10" height="10" viewBox="0 0 12 12"><circle cx="6" cy="6" r="6"/><path d="M3.2 6.2 5.2 8 8.8 4" stroke="#fff" stroke-width="1.5" fill="none"/></svg><span>„Coaching? Vielleicht bringt es ja wenigstens etwas Struktur in meine<br>Gedanken.“</span></li>
  </ul>
</main>

</body>
</html>
```